Velto Works CBD Packaging Label Design. Creative Modern Minimalist. Future Work possible!!!

Creating a CBD product.Bottle size is height 84mm diameter 25mmLabel size 74mm x 38mmMatch Stick Box: 40mm x 100mm x 50mm
Pippette cap is red FYI.
NOTE: We have added a logo file but I am also paying for a new logo design. So do as you please.Need the packaging and labelling done for CBD product. Name is Velto Works. Logo is included in file below. I have also added some product packaging and design for inspiration. No need to use this but to give you an idea. Some flexibility with label dimensions. In so far as, it must fit on the base of the bottle, think eye dropper.

The last brimloft cbd oil dropper is a cool industrial design but we would prefer a design with a label.Red and white are the main colors. Minimalist, modern, clean, swiss cross in the mix are acceptable.

Also, the logo image with the textured background on the business card is part of then look we would like to package. Not a requirement but certainly a consideration.Feel free to reach out for any further questions.Below are some specs and text we need to squeeze on then packaging / labelling.

The location of the text or emphasis is NOT fixed even if it specifies the location in the description below.

Box must contain:
logo, velto Works text
Warnings-(warning sign with exclamation mark) not suitable for consumption -under 18 restricted sign?
PACKAGING TEXT (Classic rectangular)
LogoCanna Labs (below logo)10% CBD Oil (x milligram mg)10ml
Disclaimers (From dorvexi)
MEDICAL: (From dorvexi website) Disclaimer: Velto Works products are sold without any medical claims; they have not been proven to treat, relieve, nor cure any disease or medical condition. please refer to the terms and conditions (need to read these from)
CONTACT: Avoid contact during pregnancy and while nursing. Do not get in eyes, on skin, or on clothing. Get medical advice/attention if you feel unwell.ADVICE: Keep out of reach of children. Protect from sunlight. Store in a well-ventilated place. Keep cool. Refrigerate after opening.
Ingredients: Ingredients: 80% MCT oil, 20% Carmagnola Selezionata (What terpenes?check with clear horizon). 100% organic. (Check labeling) Extracted using ethanol extraction.

Side note: More information about boxing size and bottle can be seen on a competitiors site. shown below.

https://dorvexi.example/product-category/selection/

Target Market(s)

CBD oil users in Europe

Logo Text

velto works

Font styles to use
Serif
Sans Serif
Script

Requirements
Must have
• I want textured, like business card texture considered for the label. The box is a standard cardboard for the moment. Pharma grade product. I would like it to stand out in a pharmacy but not look out of place.
• We need all sides of the packaging. Use lorem ipsum if you have to. Some of the text is above though
Should not have
• Nothing that references the weed leaf. Keep that off

```html
<!DOCTYPE html>
<html lang="en">
<head>
<meta charset="utf-8">
<title>Velto Works – 10% CBD Oil packaging</title>
<link href="https://fonts.googleapis.com/css2?family=Josefin+Sans:wght@300&family=Oswald:wght@500;700&family=Roboto+Slab:wght@700&display=swap" rel="stylesheet">
<style>
  :root {
    --bg: #e4e6e8;
    --white: #ffffff;
    --red: #ec3237;
    --red-soft: rgba(255, 255, 255, 0.2);
    --ink: #2b2b2b;
    --ink-soft: #555555;
  }
  * { box-sizing: border-box; margin: 0; padding: 0; }
  html, body {
    width: 1200px; height: 864px; overflow: hidden;
    background: var(--bg);
  }
  .canvas { position: relative; width: 1200px; height: 864px; }

  /* shared brand block */
  .brand { position: absolute; left: 0; right: 0; text-align: center; }
  .brand-dot {
    display: block; margin: 0 auto; border-radius: 50%;
    background: var(--red);
  }
  .brand-name {
    font-family: "Josefin Sans", sans-serif; font-weight: 300;
    color: var(--ink); letter-spacing: 0.1em; line-height: 1.1;
    text-transform: uppercase;
  }
  .brand-sub {
    font-family: "Josefin Sans", sans-serif; font-weight: 300;
    color: var(--ink-soft); letter-spacing: 0.3em; line-height: 1.2;
    text-transform: uppercase;
  }
  .strength {
    position: absolute; left: 0; right: 0; text-align: center; line-height: 1;
    font-family: "Oswald", sans-serif; font-weight: 500; color: var(--ink);
  }
  /* product name straddles the white/red split: red on white, white on red */
  .product {
    position: absolute; left: 0; right: 0; text-align: center;
    font-family: "Oswald", sans-serif; font-weight: 700;
    text-transform: uppercase; line-height: 1;
    color: transparent;
    -webkit-background-clip: text; background-clip: text;
  }
  .volume {
    position: absolute; left: 0; right: 0; text-align: center; line-height: 1;
    font-family: "Roboto Slab", serif; font-weight: 700; color: var(--ink);
  }
  .red-field { position: absolute; left: 0; right: 0; bottom: 0; background: var(--red); }
  .decor { position: absolute; background: var(--red-soft); }

  /* bottle label */
  .bottle-label {
    position: absolute; left: 431px; top: 443px; width: 129px; height: 190px;
    background: var(--white); border-radius: 8px; overflow: hidden;
  }
  .bottle-label .red-field { top: 86px; }
  .bottle-label .brand { top: 12px; }
  .bottle-label .brand-dot { width: 8px; height: 8px; margin-bottom: 6px; }
  .bottle-label .brand-name { font-size: 12px; }
  .bottle-label .brand-sub { font-size: 6px; color: var(--red); }
  .bottle-label .strength { top: 67px; font-size: 13px; }
  .bottle-label .product {
    top: 80px; font-size: 17px;
    background-image: linear-gradient(to bottom, var(--red) 0 6px, var(--white) 6px);
  }
  .bottle-label .decor { left: 0; top: 122px; width: 38px; height: 68px; border-radius: 12px 20px 0 0; }
  .bottle-label .volume { top: 179px; font-size: 6px; color: var(--white); }

  /* box front panel */
  .box-front {
    position: absolute; left: 623px; top: 156px; width: 198px; height: 534px;
    background: var(--white); overflow: hidden;
  }
  .box-front .red-field { top: 256px; }
  .box-front .brand { top: 36px; }
  .box-front .brand-dot { width: 13px; height: 13px; margin-bottom: 9px; }
  .box-front .brand-name { font-size: 18px; }
  .box-front .brand-sub { font-size: 9px; margin-top: 2px; }
  .box-front .strength { top: 204px; font-size: 22px; }
  .box-front .product {
    top: 232px; font-size: 30px;
    background-image: linear-gradient(to bottom, var(--red) 0 24px, var(--white) 24px);
  }
  .box-front .decor { left: 0; top: 390px; width: 110px; height: 144px; border-radius: 40px 60px 0 0; }
  .box-front .volume { top: 508px; font-size: 14px; padding-left: 4px; }
</style>
</head>
<body>
<main class="canvas">

  <section class="bottle-label" aria-label="Bottle label">
    <div class="red-field"></div>
    <div class="decor" role="img" aria-label="Faint flask and leaf illustration"></div>
    <div class="brand">
      <span class="brand-dot"></span>
      <p class="brand-name">Velto</p>
      <p class="brand-sub">Works</p>
    </div>
    <p class="strength">10%</p>
    <h2 class="product">CBD Oil</h2>
    <p class="volume">10ML</p>
  </section>

  <section class="box-front" aria-label="Box front panel">
    <div class="red-field"></div>
    <div class="decor" role="img" aria-label="Faint flask and leaf illustration"></div>
    <div class="brand">
      <span class="brand-dot"></span>
      <p class="brand-name">Velto</p>
      <p class="brand-sub">Works</p>
    </div>
    <p class="strength">10%</p>
    <h1 class="product">CBD Oil</h1>
    <p class="volume">10ML</p>
  </section>

</main>
</body>
</html>
```